quorvadeal.com redesign with wireframes, white space and custom form are very important

Need a new two column design that will convert easily to mobile responsive. Lots of white space. Winning design will probably be based on header area and making the custom form stand out. I want the header to be very much like www.talbekmo.com except the form not to go up into the header.
Here are some of the websites I really like:
www.pivrostacks.com
http://glendarokfastmove.com/
http://morquilandestate.com/

We buy homes for cash and close fast. Our target is a home seller who is desperate to sell quickly.
I have uploaded my really ugly wireframe and my logo. I also uploaded my photo for the about us box and a possible photo to use for the header.
The copy on the wireframe is what I will be using except for the about us box.

Here is the exact link for video to frame in the top left box.
https://example-vidhost.net/Kp39xqTzR2a

Number of Pages Required

1 page

Font styles to use
Sans Serif

Colors
0592cd
85cae6
eaf1f7
fbee3d
ec1f27

Requirements
Must have
• Everything on wireframe.
• Must use Verdana font and nothing should be smaller than 12 point. Most should be in 14 point. (except maybe inside of form)

```html
<!DOCTYPE html>
<html lang="en">
<head>
<meta charset="utf-8">
<title>quorvadeal.com</title>
<link rel="stylesheet" href="https://fonts.googleapis.com/css2?family=Nunito:ital,wght@0,400;0,700;0,800;0,900;1,400;1,800&family=Montserrat:wght@400;500&display=swap">
<style>
:root{
  --accent:#ef4a2f;
  --link:#6fa3d6;
  --ink:#111;
  --text:#333;
  --page:#e9eef2;
  --panel:#fff;
  --soft:#e8ecef;
  --form-edge:#8fc3e6;
  --form-bg:#eef3f7;
  --rule:#e2e6ea;
}
*{box-sizing:border-box;margin:0;padding:0}
html,body{width:1200px;height:758px;overflow:hidden}
body{background:var(--page);font-family:'Montserrat',sans-serif;color:var(--text);position:relative}
.sheet{position:absolute;left:117px;top:0;width:960px;height:758px;background:var(--panel);border-top:5px solid var(--accent)}
.abs{position:absolute}
.brand{left:35px;top:42px;display:flex;align-items:center;gap:8px;font-family:'Nunito',sans-serif;font-weight:900;font-size:19px;color:var(--accent);white-space:nowrap}
.brand-mark{width:14px;height:14px;background:var(--accent)}
.nav{left:194px;top:60px;display:flex;gap:27px;font-family:'Nunito',sans-serif;font-weight:700;font-size:14px;color:var(--link);white-space:nowrap}
.call{left:719px;top:40px;width:240px;text-align:center;font-family:'Nunito',sans-serif;color:var(--ink);white-space:nowrap}
.call-title{font-weight:800;font-size:15px}
.call-sub{font-weight:700;font-size:13.5px;margin-top:1px}
.call-phone{color:var(--accent);font-weight:800;font-size:20.5px;margin-top:0;display:flex;align-items:center;justify-content:center;gap:6px}
.hero{left:19px;top:127px;width:922px;height:187px;background:var(--soft);padding:8px}
.hero-photo{width:100%;height:100%;background:linear-gradient(180deg,#3e73b8 0%,#6a8fb6 35%,#7a6a55 60%,#4a3a2c 80%,#8a8a86 100%);display:flex;flex-direction:column;align-items:center;justify-content:center;font-family:'Nunito',sans-serif;font-weight:900;color:#fff;text-shadow:0 2px 4px rgba(0,0,0,.6);white-space:nowrap}
.hero-title{font-size:41px;line-height:1.1}
.hero-sub{font-size:30px;margin-top:8px}
.hero-sub span{color:var(--accent)}
.side-tabs{position:absolute;left:1077px;top:175px;width:35px;background:var(--accent);border-radius:0 4px 4px 0}
.side-tabs div{height:39px;display:flex;align-items:center;justify-content:center;border-bottom:1px solid rgba(255,255,255,.35)}
.side-tabs div:last-child{border:0}
.intro{left:40px;top:356px;width:456px}
.intro h2{font-family:'Nunito',sans-serif;font-weight:800;font-size:19px;color:var(--link);margin-bottom:12px;white-space:nowrap}
.perks{list-style:none}
.perks li{display:flex;align-items:center;gap:12px;padding:0 0 0 17px;height:47px;border-bottom:1px solid var(--rule);font-size:15px;white-space:nowrap}
.perks li:last-child{border:0}
.video-note{left:37px;top:559px;width:462px;height:59px;background:var(--soft);padding:8px 13px;font-size:16px;line-height:1.4}
.video{left:37px;top:641px;width:463px;height:130px;background:var(--soft);padding:8px 8px 0}
.video-frame{width:100%;height:100%;background:linear-gradient(90deg,#000 0 10%,#8fd0e8 10% 88%,#000 88%);position:relative}
.play{position:absolute;left:185px;bottom:-10px;width:79px;height:20px;background:var(--accent);border-radius:5px}
.offer{left:578px;top:353px;width:343px}
.offer-head{height:52px;background:var(--accent);border-radius:4px 4px 0 0;position:relative;display:flex;align-items:center;justify-content:center;font-family:'Nunito',sans-serif;font-weight:800;font-size:18px;color:#fff;white-space:nowrap}
.offer-head em{font-weight:800;font-size:21px;margin-right:7px}
.offer-head:after{content:"";position:absolute;left:38px;bottom:-7px;border:7px solid transparent;border-bottom:0;border-top-color:var(--accent)}
.offer-body{background:var(--form-bg);border:5px solid var(--form-edge);border-top:0;height:360px;padding:14px 13px}
.offer-body h3{font-family:'Nunito',sans-serif;font-weight:700;font-size:19px;color:var(--ink);text-align:center;line-height:1.2;margin-bottom:16px}
.field{display:block;width:100%;height:35px;background:#fff;border:1px solid #dde3e8;margin-bottom:11px;padding:0 13px;font-family:'Nunito',sans-serif;font-style:italic;font-size:12px;letter-spacing:-.1px;color:#666;line-height:33px;white-space:nowrap;overflow:hidden}
</style>
</head>
<body>
<div class="sheet">
  <div class="abs brand"><span class="brand-mark"></span>quorvadeal.com</div>
  <nav class="abs nav"><span>Sell Your Home</span><span>How it Works</span><span>Stop Foreclosure</span><span>Probate</span><span>Contact</span></nav>
  <div class="abs call">
    <div class="call-title">Call Us!</div>
    <div class="call-sub">Nights and Weekends ok</div>
    <div class="call-phone"><svg width="15" height="15" viewBox="0 0 16 16"><circle cx="8" cy="8" r="8" fill="#ef4a2f"/><path d="M5 4.2l1.4-.4 1 2.1-.9.8c.4 1 1.1 1.7 2 2.1l.8-.9 2.1 1-.4 1.4c-3 .3-6.3-3-6-6.1z" fill="#fff"/></svg>555-013-4728</div>
  </div>
  <div class="abs hero">
    <div class="hero-photo" role="img" aria-label="Photo of a house front under a blue sky">
      <div class="hero-title">Sell Your Home For Cash in 8 Days</div>
      <div class="hero-sub">We Buy Houses <span>Nationwide</span></div>
    </div>
  </div>
  <section class="abs intro">
    <h2>We are the Fastest Home Buyers Around!</h2>
    <ul class="perks">
      <li><svg width="20" height="20" viewBox="0 0 20 20"><circle cx="10" cy="10" r="10" fill="#ef4a2f"/><path d="M5.5 10.5l3 3 6-7" stroke="#fff" stroke-width="2.4" fill="none"/></svg>You pick the closing date</li>
      <li><svg width="20" height="20" viewBox="0 0 20 20"><circle cx="10" cy="10" r="10" fill="#ef4a2f"/><path d="M5.5 10.5l3 3 6-7" stroke="#fff" stroke-width="2.4" fill="none"/></svg>You pay NO commissions or fees</li>
      <li><svg width="20" height="20" viewBox="0 0 20 20"><circle cx="10" cy="10" r="10" fill="#ef4a2f"/><path d="M5.5 10.5l3 3 6-7" stroke="#fff" stroke-width="2.4" fill="none"/></svg>You don’t have to paint, clean or make repairs</li>
    </ul>
  </section>
  <div class="abs video-note">Watch to see our president Marcus explain how easy it is to sell to us.</div>
  <div class="abs video">
    <div class="video-frame" role="img" aria-label="Video of the company president speaking in front of a house"><span class="play"></span></div>
  </div>
  <form class="abs offer">
    <div class="offer-head"><em>Yes!</em> I want to sell my home fast!</div>
    <div class="offer-body">
      <h3>Get a no obligation written offer<br>in 36 hours...</h3>
      <span class="field">Your Name</span>
      <span class="field">Your phone number</span>
      <span class="field">Your Email Address</span>
      <span class="field">Property Address including City, State and Zip Code</span>
      <span class="field">Repairs needed if any</span>
      <span class="field">Asking price</span>
    </div>
  </form>
</div>
<div class="side-tabs">
  <div><svg width="18" height="18" viewBox="0 0 16 16"><circle cx="8" cy="8" r="8" fill="#fff"/><path d="M5 4.2l1.4-.4 1 2.1-.9.8c.4 1 1.1 1.7 2 2.1l.8-.9 2.1 1-.4 1.4c-3 .3-6.3-3-6-6.1z" fill="#ef4a2f"/></svg></div>
  <div><svg width="17" height="13" viewBox="0 0 17 13"><rect width="17" height="13" rx="1.5" fill="#fff"/><path d="M1 1.5l7.5 5.5L16 1.5" stroke="#ef4a2f" stroke-width="1.5" fill="none"/></svg></div>
</div>
</body>
</html>
```